Modern card design needed for building development company

We are looking for a sharp modern new look for our business cards.
We are a New Zealand based company called TKV Ventures NZ LTD that specialises in subdividing large sections, housing and commercial buildings.
We have attached a photo of the current logo and would like to see it improved somehow as it looks a bit dated.
We are open to any colours.

Target Market(s)

Investors, Property buyers

Industry/Entity Type

Investment

Contact Information for Business Card

TKV VENTURES NZ LTD
www.tkvventuresnz.co.nz

Howard Pennick
Phone +64 21 843 192
Email hdpennick@fernmail.co.nz

Font styles to use
Serif
Sans Serif

Colors
0792cd
33a6d7
85cae6
6b449b
886aae
f04a50
ec1f27
f37122
f68d4d

Requirements
Must have
• Please try and make the logo more modern or if you have a similar one we would like to see it.

```html
<!DOCTYPE html>
<html lang="en">
<head>
<meta charset="utf-8">
<title>TKV Ventures NZ LTD – Business Card</title>
<link href="https://fonts.googleapis.com/css2?family=Oswald:wght@600&family=Open+Sans:wght@400&display=swap" rel="stylesheet">
<style>
  :root {
    --page-bg: #2a2a2c;
    --card-white: #ffffff;
    --card-black: #1b1b1c;
    --ink-dark: #1f1f1f;
    --ink-light: #f4f4f4;
    --brand-blue: #0792cd;
    --brand-blue-light: #33a6d7;
    --brand-purple: #6b449b;
  }
  * { box-sizing: border-box; margin: 0; padding: 0; }
  html, body { width: 1200px; height: 900px; overflow: hidden; }
  body {
    background: var(--page-bg);
    position: relative;
    font-family: "Open Sans", sans-serif;
  }
  .card {
    position: absolute;
    width: 620px;
    height: 354px;
    overflow: hidden;
    box-shadow: 0 10px 30px rgba(0,0,0,.45);
  }
  .card-front {
    left: 70px; top: 90px;
    background: var(--card-white);
    border-left: 6px solid var(--brand-purple);
    border-right: 6px solid var(--brand-blue);
    display: flex;
    flex-direction: column;
    align-items: center;
    justify-content: center;
  }
  .card-back {
    left: 510px; top: 456px;
    background: var(--card-black);
  }
  .brand {
    display: flex;
    align-items: center;
    gap: 14px;
  }
  .brand-square {
    width: 30px; height: 30px;
    background: var(--brand-blue);
  }
  .brand-name {
    font-family: "Oswald", sans-serif;
    font-weight: 600;
    font-size: 34px;
    letter-spacing: .5px;
    color: var(--ink-dark);
  }
  .card-back .brand-name { color: var(--ink-light); }
  .front-web {
    margin-top: 10px;
    font-size: 21px;
    color: var(--ink-dark);
    letter-spacing: .3px;
  }
  .back-content {
    position: absolute;
    left: 0; right: 0; top: 52px;
    display: flex;
    flex-direction: column;
    align-items: center;
  }
  .contact-list {
    list-style: none;
    margin-top: 24px;
    color: var(--ink-light);
    font-size: 14px;
    line-height: 1.85;
  }
  .contact-list li { display: flex; align-items: center; gap: 10px; }
  .contact-list svg { width: 14px; height: 14px; fill: var(--ink-light); flex: none; }
  .back-band {
    position: absolute;
    left: 0; right: 0; bottom: 0;
    height: 68px;
    background: linear-gradient(90deg, var(--brand-blue-light), var(--brand-blue));
  }
</style>
</head>
<body>

<section class="card card-front" aria-label="Business card front">
  <div class="brand">
    <span class="brand-square"></span>
    <span class="brand-name">TKV VENTURES NZ LTD</span>
  </div>
  <p class="front-web">www.tkvventuresnz.co.nz</p>
</section>

<section class="card card-back" aria-label="Business card back">
  <div class="back-content">
    <div class="brand">
      <span class="brand-square"></span>
      <span class="brand-name">TKV VENTURES NZ LTD</span>
    </div>
    <ul class="contact-list">
      <li>
        <svg viewBox="0 0 16 16" aria-hidden="true"><path d="M3.5 1.5l2.5 0 1 3.5-1.8 1.3a8 8 0 0 0 4.5 4.5L11 9l3.5 1v2.5A2 2 0 0 1 12.5 14.5 11 11 0 0 1 1.5 3.5a2 2 0 0 1 2-2z"/></svg>
        +64 21 843 192
      </li>
      <li>
        <svg viewBox="0 0 16 16" aria-hidden="true"><path d="M1 3h14v10H1z M2.5 4.5 8 8.5l5.5-4" fill="none" stroke="#f4f4f4" stroke-width="1.4"/></svg>
        hdpennick@fernmail.co.nz
      </li>
      <li>
        <svg viewBox="0 0 16 16" aria-hidden="true"><g fill="none" stroke="#f4f4f4" stroke-width="1.3"><circle cx="8" cy="8" r="6.5"/><ellipse cx="8" cy="8" rx="2.8" ry="6.5"/><path d="M1.5 8h13M2.5 4.8h11M2.5 11.2h11"/></g></svg>
        www.tkvventuresnz.co.nz
      </li>
      <li>
        <svg viewBox="0 0 16 16" aria-hidden="true"><path d="M8 0.8a5 5 0 0 1 5 5c0 3.6-5 9.4-5 9.4S3 9.4 3 5.8a5 5 0 0 1 5-5zm0 3a2 2 0 1 0 0 4 2 2 0 0 0 0-4z"/></svg>
        PO BOX 48215, Devonport, Auckland, New Zealand
      </li>
    </ul>
  </div>
  <div class="back-band"></div>
</section>

</body>
</html>
```